Verelto Services

Double sided business cards with color on front and black and white on back. I have basic ideas and graphics, but am looking for someone to take them to the next level

```html
<!DOCTYPE html>
<html lang="en">
<head>
<meta charset="utf-8">
<title>Verelto Services – Business Cards</title>
<link href="https://fonts.googleapis.com/css2?family=Jost:wght@300;400;700&display=swap" rel="stylesheet">
<style>
  :root {
    --ink: #0b0b0b;
    --paper: #f1f1f1;
    --rule-dark: #3a3a3a;
    --rule-light: #9a9a9a;
    --backdrop: #bdbdbd;
    --sphere-a: #8a6fd1;
    --sphere-b: #f0b34a;
    --sphere-c: #5cc28b;
  }
  * { box-sizing: border-box; margin: 0; padding: 0; }
  html, body { width: 1200px; height: 1005px; overflow: hidden; }
  body {
    background: var(--backdrop);
    font-family: "Jost", sans-serif;
    position: relative;
  }
  .card {
    position: absolute;
    left: 280px;
    width: 640px;
    height: 366px;
    background: var(--paper);
    overflow: hidden;
    box-shadow: 0 10px 30px rgba(0,0,0,0.25);
  }
  .card--back { top: 110px; }
  .card--front { top: 526px; }

  /* back side */
  .back-band {
    position: absolute; left: 0; top: 0; width: 100%; height: 150px;
    background: var(--ink);
  }
  .back-mark {
    position: absolute; left: 256px; top: 36px;
    width: 128px; height: 128px; border-radius: 50%;
    background: var(--paper);
    display: flex; align-items: center; justify-content: center;
  }
  .back-mark__disc {
    width: 112px; height: 112px; border-radius: 50%;
    background: var(--ink);
    color: var(--paper);
    font-weight: 700; font-size: 17px; letter-spacing: 1.5px;
    display: flex; align-items: center; justify-content: center;
  }
  .tagline {
    position: absolute; left: 0; width: 100%;
    text-align: center; color: var(--ink);
    font-weight: 300; font-size: 17px; letter-spacing: 0.5px;
    text-transform: uppercase;
  }
  .tagline--first { top: 200px; }
  .tagline--second { top: 226px; }
  .rule { position: absolute; height: 1px; }
  .rule--dark { background: var(--rule-dark); }
  .rule--light { background: var(--rule-light); }

  /* front side */
  .front-band {
    position: absolute; left: 0; top: 215px; width: 100%; height: 151px;
    background: var(--ink);
  }
  .company-name {
    position: absolute; left: 0; top: 110px; width: 100%;
    text-align: center; color: var(--ink);
    font-weight: 700; font-size: 28px; letter-spacing: 0.5px;
    text-transform: uppercase;
  }
  .front-mark {
    position: absolute; left: 290px; top: 150px;
    width: 134px; height: 134px; border-radius: 50%;
    background: var(--paper);
    display: flex; align-items: center; justify-content: center;
  }
  .front-mark__art {
    width: 116px; height: 116px; border-radius: 50%;
    background: radial-gradient(circle at 35% 40%, var(--sphere-c), var(--sphere-a) 55%, var(--sphere-b));
    opacity: 0.55;
  }
  .phone {
    position: absolute; left: 0; top: 292px; width: 100%;
    text-align: center; color: var(--paper);
    font-weight: 300; font-size: 34px; letter-spacing: 2px;
  }
</style>
</head>
<body>

  <section class="card card--back" aria-label="Card back">
    <div class="back-band"></div>
    <div class="back-mark">
      <div class="back-mark__disc">VERELTO</div>
    </div>
    <p class="tagline tagline--first">A Curated Experience</p>
    <p class="tagline tagline--second">All That Is Promised Is Clarity</p>
    <div class="rule rule--dark" style="left:0; top:239px; width:150px;"></div>
    <div class="rule rule--dark" style="left:490px; top:239px; width:150px;"></div>
    <div class="rule rule--dark" style="left:0; top:320px; width:200px;"></div>
  </section>

  <section class="card card--front" aria-label="Card front">
    <div class="front-band"></div>
    <h1 class="company-name">Verelto Services</h1>
    <div class="front-mark">
      <div class="front-mark__art" role="img" aria-label="Colourful woven sphere illustration"></div>
    </div>
    <p class="phone">555-014-7720</p>
    <div class="rule rule--light" style="left:0; top:315px; width:190px;"></div>
    <div class="rule rule--light" style="left:450px; top:315px; width:190px;"></div>
    <div class="rule rule--light" style="left:0; top:350px; width:640px;"></div>
  </section>

</body>
</html>
```